Business Consulting Website Design

UPDATED KEY MESSAGES:

The client has decided o a different direction.

The Key Messages include:
-- Creating something unique.
Every company is unique, ever culture unique. Every project customized to meet the unique needs of the client. No two things are alike.
-- One of a kind
Because every company is different, every culture is different, every objective is unique
-- Customized solutions
We create something just for you …

I think the approach needs to be about creating a masterpiece as opposed to nurturing/growing.

Perhaps we could have different abstract/colorful paint items that takes up part of the page for each landing page. Against white and on the white is where we put our text.

Client also has created a Pixelgrove Lightbox with images that she likes

http://www.pixelgrove-example.com/public_board.mhtml?code=a7c2e9f04b8d13562e7f90a1c4d6b852&board_id=58217409

She also likes the watercolor look against white background.

===============================
Need a Homepage and an Interior page redesign for my client: http://www.brightwavecounsel-example.com

Client does leadership development, performance management, talent development, etc. Has some great clients.

- This site is very old and needs a modern look. Update look & colors. She wants simple but not bland.
- Banner images should be interesting.
- She likes the purple in her logo
- She thinks Arial font is outdated and boring
- We will be rewriting all the copy.
- Design should include ProLinker icon, phone, email, and address
- She likes the client grid on the Our Clients page. We will be redoing this.

- Menus will include:
-- Home
-- What We Do
-- Who We Are
-- Our Clients
-- Snapshots (these are case studies)

One of the sites she liked is http://lanternfold-novel-example.com, though this website has much more content than she will have.

I'm attaching the following files for your reference:
- Her new business card proof that contains her logo
- a zip file containing some stock image comps

Need strong design. Site will likely be built in Wordpress.

Thanks,
Nora
Updates

Target Market(s)

SVP of Human Resources or Head of Talent

Industry/Entity Type

Business

Number of Pages Required

2 page

Font styles to use
Sans Serif

Colors
b768aa
876aae
6b449b
f04a50
f37122

Requirements
Must have
• - Designer must read the brief
• - Use logo
Nice to have
• - Strong banner images to complement the key message
• - Design will function work on mobile easily
Should not have
• - Should not look like a design template was purchased from layoutbazaar-example.com or other template sites.
• - Should not be too masculine
• - Should not feel cluttered.

```html
<!DOCTYPE html>
<html lang="en">
<head>
<meta charset="utf-8">
<title>Brightwave Counsel — Home</title>
<link rel="stylesheet" href="https://fonts.googleapis.com/css2?family=Montserrat:ital,wght@0,400;0,500;0,600;0,700;1,700&display=swap">
<style>
  :root {
    --purple-deep: #5b2d8c;
    --purple-mid: #6b449b;
    --purple-band: #7a5fa0;
    --mauve: #b768aa;
    --rose-band: #bf6a93;
    --magenta: #d64fa0;
    --coral: #f04a50;
    --nav-top: #c77fb4;
    --nav-bottom: #a95b9d;
    --text-grey: #555555;
    --rule-grey: #d6d6d6;
    --circle-grey: #a3a3a3;
    --circle-text: #2d2d2d;
    --peach: #f5b28c;
    --white: #ffffff;
  }
  * { margin: 0; padding: 0; box-sizing: border-box; }
  html, body { width: 1200px; height: 2214px; overflow: hidden; background: var(--white); }
  body { position: relative; font-family: "Montserrat", sans-serif; color: var(--purple-mid); }

  .hero {
    position: absolute; left: 0; top: 0; width: 1200px; height: 890px;
    background:
      linear-gradient(180deg, rgba(255,255,255,0) 0%, rgba(255,255,255,0) 72%, #ffffff 100%),
      linear-gradient(100deg, #f6c9cc 0%, #f3d9df 30%, #ecc3d9 55%, #e3a3cb 75%, #f1d8e6 100%);
  }

  .site-nav {
    position: absolute; left: 0; top: 0; width: 1200px; height: 62px;
    background: linear-gradient(180deg, var(--nav-top), var(--nav-bottom));
  }
  .site-nav a {
    position: absolute; top: 0; line-height: 58px; transform: translateX(-50%);
    color: var(--white); text-decoration: none; font-weight: 700; font-size: 23px; white-space: nowrap;
  }

  .brand {
    position: absolute; display: flex; align-items: center; gap: 16px;
    font-weight: 600; letter-spacing: 3px; text-transform: uppercase; line-height: 1.15;
  }
  .brand-mark { width: 34px; height: 34px; flex: none; }
  .brand--header { left: 150px; top: 200px; color: var(--purple-deep); font-size: 38px; }
  .brand--header .brand-mark { background: var(--purple-deep); }
  .brand--footer { left: 110px; top: 1812px; color: var(--white); font-size: 36px; }
  .brand--footer .brand-mark { background: var(--peach); }

  .tagline {
    position: absolute; left: 0; top: 670px; width: 1200px; text-align: center;
    font-size: 45px; font-weight: 700; color: var(--purple-deep);
  }
  .tagline em { font-style: italic; }

  .btn-learn {
    position: absolute; left: 474px; top: 752px; width: 254px; height: 64px;
    border-radius: 32px; background: linear-gradient(180deg, #8e5fae, #5b2d8c);
    box-shadow: 0 4px 8px rgba(60,20,80,.35);
    color: var(--white); font-weight: 700; font-size: 26px;
    display: flex; align-items: center; padding-left: 30px; gap: 16px;
  }
  .btn-learn svg { width: 46px; height: 46px; }

  .intro {
    position: absolute; left: 0; top: 925px; width: 1200px; text-align: center;
    font-size: 26px; font-weight: 600; line-height: 37px; color: var(--purple-mid);
  }

  .offer-box {
    position: absolute; left: 51px; top: 1144px; width: 1105px; height: 104px;
    border: 2px solid var(--rule-grey);
  }
  .offer-title {
    position: absolute; left: 50%; top: -19px; transform: translateX(-50%);
    background: var(--white); padding: 0 58px; white-space: nowrap;
    font-size: 26px; font-weight: 700; color: var(--purple-deep); letter-spacing: 1px;
  }
  .offer-text {
    position: absolute; left: 0; top: 52px; width: 100%; text-align: center;
    font-size: 23px; color: var(--text-grey);
  }

  .values {
    position: absolute; left: 0; top: 1308px; width: 1200px; height: 238px;
    background: linear-gradient(90deg, #0e0e0e 0%, #2b2b2b 50%, #6e6e6e 85%, #8a8a8a 100%);
  }
  .value-circle {
    position: absolute; width: 178px; height: 178px; border-radius: 50%; top: 30px;
    background: var(--circle-grey); opacity: .92;
    display: flex; align-items: center; justify-content: center; text-align: center;
    color: var(--circle-text); font-size: 21px; font-weight: 500; line-height: 29px;
  }

  .services-band {
    position: absolute; left: 0; top: 1550px; width: 1200px; height: 148px;
    background: var(--rose-band); color: var(--white); text-align: center;
  }
  .services-kicker { position: absolute; top: 32px; width: 100%; font-size: 22px; font-weight: 600; letter-spacing: 5px; }
  .services-title { position: absolute; top: 66px; width: 100%; font-size: 37px; font-weight: 700; letter-spacing: 1px; }

  .contact-band {
    position: absolute; left: 0; top: 1698px; width: 1200px; height: 340px;
    background: var(--purple-band);
  }
  .contact-rule { position: absolute; left: 534px; width: 348px; height: 2px; background: rgba(255,255,255,.35); }
  .contact-phone {
    position: absolute; left: 530px; top: 1800px; display: flex; align-items: center; gap: 16px;
    color: var(--white); font-size: 46px; font-weight: 500;
  }
  .contact-phone svg { width: 44px; height: 48px; }
  .contact-email {
    position: absolute; left: 527px; top: 1902px; white-space: nowrap;
    color: var(--white); font-size: 28px; font-weight: 500;
  }

  .site-footer {
    position: absolute; left: 0; top: 2056px; width: 1200px; text-align: center;
    font-size: 16px; line-height: 22px; color: #333333;
  }
</style>
</head>
<body>
  <div class="hero" role="img" aria-label="Watercolor photo: a makeup brush sweeping pink, magenta and coral paint across white paper"></div>

  <nav class="site-nav">
    <a href="#" style="left:235px">Home</a>
    <a href="#" style="left:399px">What We Do</a>
    <a href="#" style="left:585px">Who We Are</a>
    <a href="#" style="left:775px">Our Clients</a>
    <a href="#" style="left:941px">Snapshots</a>
  </nav>

  <div class="brand brand--header"><span class="brand-mark"></span><span>Brightwave<br>Counsel</span></div>

  <h1 class="tagline"><em>Creating</em>......just for you</h1>

  <a class="btn-learn">Learn More
    <svg viewBox="0 0 46 46"><circle cx="23" cy="23" r="21" fill="#ffffff"/><path d="M18 13 L28 23 L18 33" fill="none" stroke="#5b2d8c" stroke-width="5" stroke-linecap="round" stroke-linejoin="round"/></svg>
  </a>

  <p class="intro">We works on the frontlines of international development.<br>Transforming ideas into action—action into impact.<br>We are committed to shaping a more livable world.</p>

  <section class="offer-box">
    <h2 class="offer-title">WHAT CAN BWC DO FOR YOU?</h2>
    <p class="offer-text">We will craft a customized plan of services to meet each client’s unique needs.</p>
  </section>

  <section class="values" role="img" aria-label="Black and white photo of sharpened pencils with one purple pencil">
    <div class="value-circle" style="left:219px">Experience<br>Counts</div>
    <div class="value-circle" style="left:411px">Exceptional<br>Service</div>
    <div class="value-circle" style="left:631px">On time<br>On budget</div>
    <div class="value-circle" style="left:810px">Your<br>Resource</div>
  </section>

  <section class="services-band">
    <p class="services-kicker">designing, developing &amp; implementing</p>
    <p class="services-title">HUMAN RESOURCE COMMUNICATIONS</p>
  </section>

  <section class="contact-band"></section>
  <div class="brand brand--footer"><span class="brand-mark"></span><span>Brightwave<br>Counsel</span></div>
  <div class="contact-rule" style="top:1782px"></div>
  <div class="contact-phone">
    <svg viewBox="0 0 44 48"><path d="M10 4 C6 4 3 8 3 13 C3 28 16 44 32 44 C37 44 41 41 41 37 L41 33 L31 28 L26 33 C20 30 15 24 13 18 L18 14 L14 4 Z" fill="#f5b28c"/></svg>
    <span>555.214.0396</span>
  </div>
  <div class="contact-rule" style="top:1889px"></div>
  <div class="contact-email">Lena@BrightwaveCounsel-example.com</div>

  <footer class="site-footer">
    <p>Copyright &nbsp;2015, Brightwave Counsel.</p>
    <p>Legal conditions and terms of use applicable to all users of this site.</p>
    <p>Any use of this site constitutes your agreement to the terms and conditions and the operating policies.</p>
  </footer>
</body>
</html>
```